Top Real Estate teams new cards UPDATED

New Cards with MY (Im the tall guy in the middle) new pic on the front of card and my team pic on the back of card. Also my team name on the front of the card (marlow and partners) and brokerage name on the back (harborline real estate group) . Also the tag line "Ask about our 20 step plan" on the back of the card and "Welcome to the new way of Real Estate Sales" on the front of the card along with my phone number (951-284-7310) and email address (devon.marlow47@quillmail.net) my website (www.DevonMarlow.org) and my License number (BRE:07315942). I do like my team name colors of black and gold
Logo links are attached:
1. https://www.filecrate.net/sh/918kqwz72pavdle/AAF7QmR2HtK4BnYwPzLxUe_KGb?dl=0
2. https://www.filecrate.net/sh/27w5xvn81rbt094/AACKTJMR46DnQ2Wf7RyGs8Vh3b?dl=0
Updates

Target Market(s)

Real Estate Customers

Industry/Entity Type

Real Estate

Contact Information for Business Card

Classy, yet east ro read and understand

Font styles to use
Sans Serif

Requirements
Must have
• Team and brokerage name, and both slogans.
• Black and gold color scheme.
Nice to have
• Bold writing
Should not have
• cluttered feeling

```html
<!DOCTYPE html>
<html lang="en">
<head>
<meta charset="utf-8">
<title>Marlow and Partners – Business Card</title>
<link href="https://fonts.googleapis.com/css2?family=Montserrat:wght@400;500;600;700&display=swap" rel="stylesheet">
<style>
  :root {
    --stage: #2a2a2a;
    --ink: #0b0b0b;
    --paper: #ffffff;
    --gold: #e9e28a;
    --text-dark: #1a1a1a;
    --text-muted: #3a3a3a;
  }
  html, body {
    margin: 0;
    padding: 0;
    width: 1200px;
    height: 1200px;
    overflow: hidden;
    background: var(--stage);
    font-family: "Montserrat", sans-serif;
  }
  .canvas { position: relative; width: 1200px; height: 1200px; }
  .card {
    position: absolute;
    left: 150px;
    width: 900px;
    height: 514px;
    overflow: hidden;
    box-shadow: 0 18px 40px rgba(0,0,0,0.45);
  }
  .card--front { top: 56px; background: var(--ink); }
  .card--back  { top: 630px; background: var(--paper); }
  .card-art { position: absolute; inset: 0; width: 900px; height: 514px; }

  .brand {
    position: absolute;
    margin: 0;
    font-weight: 500;
    text-transform: uppercase;
    line-height: 1.25;
    text-align: center;
  }
  .brand-main { display: block; font-size: 40px; letter-spacing: 0.04em; }
  .brand-sub  { display: block; font-size: 17px; letter-spacing: 0.18em; margin-top: 4px; }
  .card--front .brand { color: var(--paper); left: 300px; top: 120px; width: 540px; }
  .card--back  .brand { color: var(--text-dark); right: 50px; top: 60px; width: 440px; }
  .card--back  .brand-main { font-size: 38px; }
  .card--back  .brand-sub  { font-size: 16px; }

  .tagline-front {
    position: absolute;
    right: 40px;
    top: 268px;
    margin: 0;
    color: var(--gold);
    font-size: 24px;
    font-weight: 500;
    letter-spacing: 0.02em;
  }

  .contact { position: absolute; left: 58px; top: 110px; color: var(--text-dark); }
  .contact-name { font-size: 34px; font-weight: 700; letter-spacing: 0.03em; margin: 0; }
  .contact-title { font-size: 18px; color: var(--text-muted); margin: 2px 0 6px; }
  .contact-license { font-size: 18px; margin: 0 0 8px; }
  .contact-license strong { font-weight: 700; }
  .contact-list { list-style: none; margin: 0; padding: 0; }
  .contact-list li { display: flex; align-items: center; gap: 10px; font-size: 19px; line-height: 30px; }
  .contact-list svg { width: 14px; height: 14px; flex: none; }
  .contact-list strong { font-weight: 700; }

  .tagline-back {
    position: absolute;
    right: 60px;
    bottom: 24px;
    margin: 0;
    color: var(--gold);
    font-size: 24px;
    font-weight: 500;
    letter-spacing: 0.1em;
    text-transform: uppercase;
  }
</style>
</head>
<body>
<main class="canvas">

  <section class="card card--front" aria-label="Card front">
    <svg class="card-art" viewBox="0 0 900 514" aria-hidden="true">
      <defs>
        <linearGradient id="frontInk" x1="0" y1="0" x2="1" y2="1">
          <stop offset="0" stop-color="#000"/>
          <stop offset="0.6" stop-color="#161616"/>
          <stop offset="1" stop-color="#050505"/>
        </linearGradient>
        <linearGradient id="frontSilver" x1="0" y1="0" x2="0" y2="1">
          <stop offset="0" stop-color="#7d7d7d"/>
          <stop offset="0.35" stop-color="#d8d8d8"/>
          <stop offset="1" stop-color="#f4f4f4"/>
        </linearGradient>
      </defs>
      <rect width="900" height="514" fill="url(#frontInk)"/>
      <path d="M0,365 C180,345 330,365 450,412 C580,465 720,482 900,484 L900,514 L0,514 Z" fill="url(#frontSilver)"/>
      <path d="M0,365 C180,345 330,365 450,412 C580,465 720,482 900,484" fill="none" stroke="var(--gold)" stroke-width="4"/>
    </svg>
    <h2 class="brand">
      <span class="brand-main">Marlow and Partners</span>
      <span class="brand-sub">Harborline Real Estate Group</span>
    </h2>
    <p class="tagline-front">Welcome to the new way of Real Estate Sales</p>
  </section>

  <section class="card card--back" aria-label="Card back">
    <svg class="card-art" viewBox="0 0 900 514" aria-hidden="true">
      <defs>
        <linearGradient id="backSheen" x1="0" y1="0" x2="0" y2="1">
          <stop offset="0" stop-color="#ffffff"/>
          <stop offset="1" stop-color="#bdbdbd"/>
        </linearGradient>
        <linearGradient id="backInk" x1="0" y1="0" x2="1" y2="0">
          <stop offset="0" stop-color="#000"/>
          <stop offset="0.5" stop-color="#1b1b1b"/>
          <stop offset="1" stop-color="#050505"/>
        </linearGradient>
      </defs>
      <rect width="900" height="514" fill="var(--paper)"/>
      <path d="M0,322 C110,305 190,325 260,362 C360,415 620,402 900,352 L900,514 L0,514 Z" fill="url(#backSheen)"/>
      <path d="M0,345 C110,330 190,350 260,388 C360,442 620,430 900,380 L900,514 L0,514 Z" fill="url(#backInk)"/>
    </svg>
    <h2 class="brand">
      <span class="brand-main">Harborline</span>
      <span class="brand-sub">Real Estate Group</span>
    </h2>
    <div class="contact">
      <h1 class="contact-name">Devin Hale</h1>
      <p class="contact-title">Director</p>
      <p class="contact-license"><strong>License</strong> : (BRE:07315942)</p>
      <ul class="contact-list">
        <li>
          <svg viewBox="0 0 16 16" aria-hidden="true"><path d="M3.5 1.5 L6 4 L4.6 5.8 C5.5 7.8 8.2 10.5 10.2 11.4 L12 10 L14.5 12.5 L12.8 14.5 C7 14 2 9 1.5 3.2 Z" fill="var(--text-dark)"/></svg>
          <span>951-284-7310</span>
        </li>
        <li>
          <svg viewBox="0 0 16 16" aria-hidden="true"><rect x="1.5" y="3.5" width="13" height="9" fill="none" stroke="var(--text-dark)" stroke-width="1.5"/><path d="M1.5 3.5 L8 9 L14.5 3.5" fill="none" stroke="var(--text-dark)" stroke-width="1.5"/></svg>
          <span>devon.marlow47@quillmail.net</span>
        </li>
        <li>
          <svg viewBox="0 0 16 16" aria-hidden="true"><circle cx="8" cy="8" r="6.5" fill="none" stroke="var(--text-dark)" stroke-width="1.5"/><ellipse cx="8" cy="8" rx="3" ry="6.5" fill="none" stroke="var(--text-dark)" stroke-width="1.2"/><path d="M1.5 8 H14.5" stroke="var(--text-dark)" stroke-width="1.2"/></svg>
          <span>www.<strong>DevonMarlow</strong>.org</span>
        </li>
      </ul>
    </div>
    <p class="tagline-back">Ask about our 20 step plan</p>
  </section>

</main>
</body>
</html>
```